TBL Enterprises has 5 divisions in the organisation.
One of them is our Soaps, Candles and Cosmetics range.

Our Logo is a MERIN with the word MERIN an image of a crown.
Merin Supplements & Merin Sports are 2 divisions.

Now we need to introduce our MERIN COLLECTIONS which will include cosmetic, candles, fragrances etc.

What we need designed is an elegant, sophisticated label of our CANDLE JARS and Outer Box.

The same will flow through to our soaps and other collection.

This will the beginning of a long term relationship for the designer to maintain and update our Merin Collections artwork.

Hello designers,

We have increases our 1st prize budget to $200.00

Please read the brief carefully.
We need this job wrapped up quickly.

It is a fairly simple project with huge long term potential.

We look forward to receiving some designs.

Reason: Due to the Easter Break last week, many people were off work. Therefore we have extended our deadline to allow other participants to submit their designs.

Reason: We have not found a design we like yet.

Industry/Entity Type

Cosmetics

Requirements
Must have
• The MERIN and the word MERIN must remain the same.
The word collections must be added under the crown.
The word collections to be Elegant, maybe cursive, or hand written.

Wording for Jar Label:
100% Soy Wax
Quality Essential oils & Fragrances
Hand made in Australia

Box Wording:
will be provided at later stage.
Make a mockup of a box but not too loud.
Sophisticated and elegant.
Do not use existing artwork from others.

Nice to have
• Special design label.

The width of the label to be no more than 50mm.
The height of the label to be no more than 60mm

We believe that the JAR label needs to be small and effective.
We beleive the box should use Royal colours and not too many flowers and vines. Elegance.
Should not have
• Should not be noisy, loud and full of information.

```html
<!DOCTYPE html>
<html lang="en">
<head>
<meta charset="utf-8">
<title>Merin Collections – Box and Jar Label</title>
<link rel="stylesheet" href="https://fonts.googleapis.com/css2?family=Cormorant+Garamond:wght@500&family=Josefin+Sans:wght@300&family=Oswald:wght@600&display=swap">
<style>
  :root {
    --gold: #ae9600;
    --gold-soft: rgba(174, 150, 0, 0.22);
    --heading-grey: #c4c4c4;
    --copy-grey: #8f8f8f;
    --ink: #1f1f1f;
    --paper: #ffffff;
  }
  * { margin: 0; padding: 0; box-sizing: border-box; }
  html, body { width: 1200px; height: 1000px; overflow: hidden; background: var(--paper); }
  .sheet { position: relative; width: 1200px; height: 1000px; background: var(--paper); }
  .frames { position: absolute; inset: 0; }
  .section-heading {
    position: absolute;
    font-family: "Oswald", sans-serif;
    font-weight: 600;
    color: var(--heading-grey);
    letter-spacing: 2px;
    line-height: 1;
  }
  .section-heading--box { left: 220px; top: 30px; font-size: 64px; }
  .section-heading--label { left: 818px; top: 236px; font-size: 64px; }

  .wordmark {
    position: absolute;
    text-align: center;
    font-family: "Cormorant Garamond", serif;
    font-weight: 500;
    line-height: 1;
  }
  .wordmark__name { display: block; letter-spacing: 3px; }
  .wordmark__range { display: block; letter-spacing: 1px; }

  .wordmark--box { left: 60px; width: 480px; top: 250px; color: var(--paper); }
  .wordmark--box .wordmark__name { font-size: 76px; }
  .wordmark--box .wordmark__range { font-size: 50px; margin-top: 46px; }

  .wordmark--label { left: 656px; width: 490px; top: 478px; color: var(--gold); }
  .wordmark--label .wordmark__name { font-size: 82px; }
  .wordmark--label .wordmark__range { font-size: 52px; margin-top: 44px; }

  .product-name {
    position: absolute;
    left: 60px; top: 645px; width: 480px; height: 78px;
    display: flex; align-items: center; justify-content: center;
    font-family: "Cormorant Garamond", serif;
    font-weight: 500;
    font-size: 36px;
    color: var(--ink);
    letter-spacing: 1px;
  }
  .box-footer {
    position: absolute;
    left: 60px; width: 480px; top: 864px;
    text-align: center;
    font-family: "Cormorant Garamond", serif;
    font-weight: 500;
    font-size: 23px;
    line-height: 28px;
    color: var(--gold);
  }
  .label-copy {
    position: absolute;
    left: 640px; width: 530px; top: 752px;
    text-align: center;
    font-family: "Josefin Sans", sans-serif;
    font-weight: 300;
    font-size: 30px;
    line-height: 49px;
    color: var(--copy-grey);
  }
</style>
</head>
<body>
<main class="sheet">
  <svg class="frames" width="1200" height="1000" viewBox="0 0 1200 1000" aria-hidden="true">
    <!-- outer box panel -->
    <path fill="var(--gold)" d="M96 122 L504 122 A36 36 0 0 0 540 158 L540 464 A36 36 0 0 0 504 500 L96 500 A36 36 0 0 0 60 464 L60 158 A36 36 0 0 0 96 122 Z"/>
    <path fill="none" stroke="var(--paper)" stroke-width="4" d="M100 134 L500 134 A28 28 0 0 0 528 162 L528 460 A28 28 0 0 0 500 488 L100 488 A28 28 0 0 0 72 460 L72 162 A28 28 0 0 0 100 134 Z"/>
    <line x1="190" y1="354" x2="410" y2="354" stroke="var(--paper)" stroke-width="3"/>

    <!-- jar label frame -->
    <path fill="none" stroke="var(--gold)" stroke-width="8" d="M698 349 L1104 349 A38 38 0 0 0 1142 387 L1142 688 A38 38 0 0 0 1104 726 L698 726 A38 38 0 0 0 660 688 L660 387 A38 38 0 0 0 698 349 Z"/>
    <line x1="786" y1="582" x2="1016" y2="582" stroke="var(--gold)" stroke-width="3"/>
    <line x1="838" y1="911" x2="970" y2="911" stroke="var(--gold)" stroke-width="2"/>

    <!-- product name band -->
    <rect x="62.5" y="647.5" width="475" height="73" fill="var(--paper)" stroke="var(--gold)" stroke-width="5"/>
  </svg>

  <div class="section-heading section-heading--box">BOX</div>
  <div class="section-heading section-heading--label">LABEL</div>

  <div class="wordmark wordmark--box">
    <span class="wordmark__name">MERIN</span>
    <span class="wordmark__range">COLLECTIONS</span>
  </div>

  <div role="img" aria-label="Gold swirling flourish ornament framing the product name band"
       style="position:absolute;left:125px;top:540px;width:335px;height:260px;border-radius:50%;background:var(--gold-soft);"></div>
  <div style="position:absolute;left:62px;top:647px;width:476px;height:74px;background:var(--paper);border:5px solid var(--gold);"></div>
  <div class="product-name">PRODUCT NAME</div>

  <p class="box-footer">ESSENTIAL OILS &amp; FRAGRANCES<br>HAND MADE IN AUSTRALIA</p>

  <div class="wordmark wordmark--label">
    <span class="wordmark__name">MERIN</span>
    <span class="wordmark__range">COLLECTIONS</span>
  </div>

  <p class="label-copy">100% Soy Wax<br>Quality Essential oils &amp; Fragrances<br>Hand made in Australia</p>
</main>
</body>
</html>
```